Corbrook Estates LLC stationary for a real estate property management company.

Create stationary (letterhead, envelopes, business cards) using Corbrook Estates LLC logo as primary creative element. Stationary design needs to be horizontal, leaving as much space as possible for correspondence copy. See attached Creative Brief and past stationary files for details.

Target Market(s)

Prospective apartment residents and current residents, vendors, and government agencies.

Industry/Entity Type

Property Management

Contact Information for Business Card

Business card employee title: Property Manager. Should include address, phone, fax, email, website, slogan, and Corbrook Estates logo.

Font styles to use
Sans Serif

Colors
0592cd
000000

Requirements
Must have
• Tone should be conservative, institutional, business (i.e. banking, finance, real estate). Must include: address, phone, fax, website, and slogan (see attached Creative Brief). Should be a horizontal design, leaving as much room as possible for letter correspondence copy.
Nice to have
• Please use an Arial or Helvetica style font.
Should not have
• Letterhead layout should leave as much room as possible for copy.

```html
<!DOCTYPE html>
<html lang="en">
<head>
<meta charset="utf-8">
<title>Corbrook Estates LLC — Stationery</title>
<link href="https://fonts.googleapis.com/css2?family=Lato:wght@400;700&display=swap" rel="stylesheet">
<style>
:root{
  --stage:#c5bfad;
  --paper:#ffffff;
  --brand-blue:#1769ae;
  --brand-dark:#454648;
  --ink:#222222;
  --faint:#eceef0;
  --pattern:#f1f2f3;
}
*{margin:0;padding:0;box-sizing:border-box}
html,body{width:1200px;height:1200px;overflow:hidden}
body{background:var(--stage);font-family:'Lato',Arial,sans-serif;color:var(--ink);position:relative}
.sheet{position:absolute;background:var(--paper);box-shadow:2px 3px 4px rgba(0,0,0,.28);overflow:hidden}
.card{width:318px;height:182px}
.brand{display:flex;align-items:center;gap:6px;color:var(--brand-blue);font-weight:700;white-space:nowrap;position:absolute}
.brand .dot{border-radius:50%;background:var(--brand-blue);flex:none}
.name{color:var(--brand-blue);font-size:12px;line-height:1.1}
.role{font-size:8px;line-height:1.2;color:var(--ink)}
.contact{position:absolute;font-size:10px;line-height:13px}
.contact .row{display:flex;align-items:center;gap:4px}
.contact .gap{height:5px}
.contact .addr{color:var(--brand-blue);margin-top:4px;line-height:12px}
.icon{width:10px;height:10px;flex:none}
.band{position:absolute;left:0;bottom:0;width:100%;height:15px}
.circle-deco{position:absolute;border-radius:50%}
</style>
</head>
<body>
<svg width="0" height="0" style="position:absolute">
  <defs>
    <symbol id="i-phone" viewBox="0 0 10 10"><rect x=".5" y=".5" width="9" height="9" rx="1" fill="#1769ae"/><path d="M2 6.5h6v1.5H2zM3 3.5h4l1 2.5H2z" fill="#fff"/></symbol>
    <symbol id="i-fax" viewBox="0 0 10 10"><rect x=".5" y=".5" width="9" height="9" rx="1" fill="#1769ae"/><rect x="2" y="4" width="6" height="4" fill="#fff"/><rect x="3" y="2" width="4" height="2" fill="#fff"/></symbol>
    <symbol id="i-mail" viewBox="0 0 10 10"><rect x=".5" y=".5" width="9" height="9" rx="1" fill="#1769ae"/><rect x="2" y="3" width="6" height="4.5" fill="#fff"/><path d="M2 3l3 2.5L8 3" stroke="#1769ae" stroke-width=".8" fill="none"/></symbol>
    <symbol id="i-web" viewBox="0 0 10 10"><rect x=".5" y=".5" width="9" height="9" rx="1" fill="#1769ae"/><circle cx="5" cy="5" r="3" stroke="#fff" stroke-width=".8" fill="none"/><path d="M2 5h6M5 2v6" stroke="#fff" stroke-width=".7"/></symbol>
  </defs>
</svg>

<!-- Business card front: personal with corner circle -->
<section class="sheet card" style="left:70px;top:52px">
  <div style="position:absolute;left:25px;top:18px">
    <div class="name">Dana Whitfield</div>
    <div class="role">Property manager</div>
  </div>
  <div class="contact" style="left:25px;top:82px">
    <div class="row"><svg class="icon"><use href="#i-phone"/></svg>555-210-4418</div>
    <div class="row"><svg class="icon"><use href="#i-fax"/></svg>555-210-4419</div>
    <div class="gap"></div>
    <div class="row"><svg class="icon"><use href="#i-mail"/></svg>dana@corbrookestates.us</div>
    <div class="row"><svg class="icon"><use href="#i-web"/></svg>www.corbrookestates.us</div>
    <div class="addr">2870 Alder Park Way #310<br>Fairview, OR 97024</div>
  </div>
  <div class="circle-deco" style="left:205px;top:60px;width:150px;height:150px;background:var(--faint)"></div>
</section>

<!-- Business card: brand left, details right -->
<section class="sheet card" style="left:443px;top:52px">
  <div class="brand" style="left:20px;top:105px;font-size:12px"><span class="dot" style="width:12px;height:12px"></span>Corbrook Estates LLC</div>
  <div style="position:absolute;left:162px;top:32px">
    <div style="font-size:11px">Dana Whitfield</div>
    <div class="role" style="font-size:9px">Property manager</div>
  </div>
  <div class="contact" style="left:162px;top:76px">
    <div class="row"><svg class="icon"><use href="#i-phone"/></svg>555-210-4418</div>
    <div class="row"><svg class="icon"><use href="#i-fax"/></svg>555-210-4419</div>
    <div class="gap"></div>
    <div class="row"><svg class="icon"><use href="#i-mail"/></svg>dana@corbrookestates.us</div>
    <div class="row"><svg class="icon"><use href="#i-web"/></svg>www.corbrookestates.us</div>
    <div class="addr">2870 Alder Park Way #310<br>Fairview, OR 97024</div>
  </div>
</section>

<!-- Business card back: pattern -->
<section class="sheet card" style="left:817px;top:52px">
  <div role="img" aria-label="Faint repeating brand pattern" style="position:absolute;inset:0;background:var(--pattern)"></div>
  <div class="brand" style="left:140px;top:150px;font-size:12px"><span class="dot" style="width:12px;height:12px"></span>Corbrook Estates LLC</div>
</section>

<!-- Business card: header brand with footer band -->
<section class="sheet card" style="left:70px;top:270px">
  <div class="brand" style="left:25px;top:24px;font-size:10px"><span class="dot" style="width:10px;height:10px"></span>Corbrook Estates LLC</div>
  <div style="position:absolute;right:22px;top:18px;text-align:right">
    <div class="name">Dana Whitfield</div>
    <div class="role">Property manager</div>
  </div>
  <div class="contact" style="left:25px;top:72px">
    <div class="row"><svg class="icon"><use href="#i-phone"/></svg>555-210-4418</div>
    <div class="row"><svg class="icon"><use href="#i-fax"/></svg>555-210-4419</div>
    <div class="gap"></div>
    <div class="row"><svg class="icon"><use href="#i-mail"/></svg>dana@corbrookestates.us</div>
    <div class="row"><svg class="icon"><use href="#i-web"/></svg>www.corbrookestates.us</div>
    <div class="addr">2870 Alder Park Way #310<br>Fairview, OR 97024</div>
  </div>
  <svg class="band" viewBox="0 0 318 15" preserveAspectRatio="none"><polygon points="0,0 232,0 225,15 0,15" fill="var(--brand-blue)"/><polygon points="234,0 318,0 318,15 227,15" fill="var(--brand-dark)"/></svg>
</section>

<!-- Business card: brand only -->
<section class="sheet card" style="left:443px;top:270px">
  <div class="brand" style="left:50px;top:78px;font-size:20px;gap:9px"><span class="dot" style="width:20px;height:20px"></span>Corbrook Estates LLC</div>
  <svg class="band" viewBox="0 0 318 15" preserveAspectRatio="none"><polygon points="0,0 232,0 225,15 0,15" fill="var(--brand-blue)"/><polygon points="234,0 318,0 318,15 227,15" fill="var(--brand-dark)"/></svg>
</section>

<!-- Letterhead -->
<section class="sheet letterhead" style="left:70px;top:513px;width:482px;height:623px">
  <div class="brand" style="left:50px;top:50px;font-size:13px"><span class="dot" style="width:13px;height:13px"></span>Corbrook Estates LLC</div>
  <div style="position:absolute;left:285px;top:46px;display:flex;font-size:7px;line-height:9px">
    <div style="padding-right:5px;border-right:1px solid var(--ink)">
      <div class="row" style="display:flex;gap:3px;align-items:center"><svg style="width:7px;height:7px"><use href="#i-phone"/></svg>555-210-4418</div>
      <div class="row" style="display:flex;gap:3px;align-items:center"><svg style="width:7px;height:7px"><use href="#i-fax"/></svg>555-210-4419</div>
    </div>
    <div style="padding-left:5px">2870 Alder Park Way #310<br>Fairview, OR 97024</div>
  </div>
  <div class="circle-deco" style="left:287px;top:296px;width:290px;height:290px;background:var(--faint)"></div>
  <svg class="band" style="height:18px" viewBox="0 0 482 18" preserveAspectRatio="none"><polygon points="0,0 345,0 338,18 0,18" fill="var(--brand-blue)"/><polygon points="347,0 482,0 482,18 340,18" fill="var(--brand-dark)"/></svg>
  <div style="position:absolute;right:40px;bottom:5px;font-size:7px;color:#fff">www.corbrookestates.us</div>
</section>

<!-- Envelope front -->
<section class="sheet envelope" style="left:602px;top:545px;width:550px;height:246px">
  <div class="brand" style="left:20px;top:30px;font-size:10px"><span class="dot" style="width:10px;height:10px"></span>Corbrook Estates LLC</div>
  <div style="position:absolute;left:145px;top:28px;padding-left:7px;border-left:1px solid var(--ink);font-size:7px;line-height:9px">2870 Alder Park Way #310<br>Fairview, OR 97024</div>
</section>

<!-- Envelope back -->
<section class="sheet envelope" style="left:602px;top:837px;width:550px;height:246px">
  <svg style="position:absolute;left:0;top:0" width="550" height="90" viewBox="0 0 550 90">
    <polygon points="0,0 550,0 543,78 536,83 14,83 8,78" fill="#fff" stroke="#d8d8d8"/>
    <line x1="14" y1="84" x2="536" y2="84" stroke="#bbb" stroke-width="2"/>
  </svg>
  <span style="position:absolute;left:258px;top:22px;width:34px;height:34px;border-radius:50%;background:var(--brand-blue)"></span>
</section>
</body>
</html>
```